Website Design - Financial Services Software

We are looking for website designs for our public website.
Some competitor sites we like are
www.torvani.com.au
www.pluma.com.au
www.quentabridge.com
www.morlupa.com.au

A wireframe example of our site can be found at
http://pr4tqz.bivlowpage.com/

Attached is our logo.

Industry/Entity Type

Financial

```html
<!DOCTYPE html>
<html lang="en">
<head>
<meta charset="utf-8">
<title>Veltora – Smarter Financial Strategies</title>
<link href="https://fonts.googleapis.com/css2?family=Open+Sans:wght@400;600&display=swap" rel="stylesheet">
<style>
:root{
  --slate:#273333;
  --slate-deep:#222d2d;
  --gold:#d7a83a;
  --gold-light:#f0d58a;
  --gold-text:#d9aa3c;
  --white:#ffffff;
  --ink:#2d3a3a;
  --ink-soft:#444f4f;
  --muted:#6d7474;
  --line:#8a8f8f;
  --footer-link:#c9cccc;
}
*{box-sizing:border-box;margin:0;padding:0}
html,body{width:1145px;height:1200px;overflow:hidden}
body{position:relative;font-family:"Open Sans",Arial,sans-serif;background:var(--slate);color:var(--white)}
a{color:inherit;text-decoration:none}
.abs{position:absolute}

/* header */
.site-header{position:absolute;left:0;top:0;width:1145px;height:136px;background:var(--slate);border-top:3px solid var(--gold)}
.brand{position:absolute;display:flex;align-items:center;gap:10px;color:var(--gold-text);font-weight:400;letter-spacing:1px}
.brand-dot{width:34px;height:34px;border-radius:50%;background:var(--gold)}
.brand-header{left:146px;top:60px;font-size:27px}
.login{position:absolute;left:923px;top:19px;width:76px;height:25px;border-radius:3px;background:linear-gradient(#f3dc93,#e3bd5a);color:#5b4a22;font-size:11.5px;text-align:center;line-height:25px}
.main-nav{position:absolute;top:69px;left:632px;height:25px;display:flex;font-size:15.5px}
.main-nav a{position:absolute;top:0;line-height:25px;white-space:nowrap}
.main-nav .active{left:0;width:75px;background:var(--white);color:#8a6016;border-radius:2px;text-align:center;font-weight:600}

/* hero */
.hero{position:absolute;left:0;top:136px;width:1145px;height:455px;background:linear-gradient(180deg,#dcdcdc 0%,#d2d2d2 45%,#a9a9a9 78%,#8d8d8d 100%)}
.hero-title{position:absolute;left:145px;top:117px;font-size:26px;font-weight:600;color:var(--ink)}
.hero-sub{position:absolute;left:146px;top:177px;width:350px;font-size:19px;line-height:36px;color:var(--ink-soft)}
.btn{position:absolute;height:36px;font-size:13.5px;text-align:center;line-height:34px;border-radius:2px}
.btn-gold{left:146px;top:287px;width:154px;background:var(--gold);border:1px solid #c0902a;color:#3e3213}
.btn-white{left:310px;top:287px;width:154px;background:var(--white);border:1px solid #bbb;color:#333}
.video{position:absolute;left:520px;top:93px;width:480px;height:276px;background:var(--white);border:1px solid #ccc;padding:9px}
.video-still{width:100%;height:100%;position:relative;background:linear-gradient(135deg,#d9dbe0 0%,#b99e7e 45%,#8c8a84 70%,#5e4b40 100%)}
.video-bar{position:absolute;left:8px;right:8px;bottom:8px;height:32px}

/* features */
.features{position:absolute;left:0;top:591px;width:1145px;height:451px;background:var(--slate);border-top:2px solid var(--gold)}
.intro-title{position:absolute;left:146px;top:36px;font-size:20.5px;font-weight:600;line-height:29px}
.intro-text{position:absolute;left:146px;width:205px;font-size:11.3px;line-height:20px}
.card{position:absolute;width:199px;height:99px;background:var(--white);border-radius:4px;color:var(--ink);padding:4px 8px}
.card.highlight{background:linear-gradient(#f6dc8f,#cf9d38)}
.card h3{font-size:15.5px;font-weight:600;color:var(--ink);line-height:22px}
.card p{font-size:10.3px;line-height:16.5px;color:var(--muted);margin-top:3px;width:140px}
.card.highlight p,.card.highlight .more{color:#7a5a1c}
.card .more{display:block;font-size:10.3px;color:var(--muted);margin-top:9px}
.card svg.icon{position:absolute;right:9px;top:26px;width:48px;height:48px}
.divider{position:absolute;left:146px;top:348px;width:853px;border-top:1px dashed var(--line)}
.cta{position:absolute;left:250px;top:385px;font-size:19px;color:var(--gold-text)}
.btn-signup{position:absolute;left:742px;top:382px;width:153px;height:35px;background:var(--white);color:#333;font-size:13px;text-align:center;line-height:35px;border-radius:2px}

/* footer */
.site-footer{position:absolute;left:0;top:1042px;width:1145px;height:158px;background:var(--slate-deep);border-top:3px solid var(--gold)}
.brand-footer{left:145px;top:54px;font-size:20px}
.brand-footer .brand-dot{width:26px;height:26px}
.foot-col{position:absolute;top:33px}
.foot-col h4{font-size:15.5px;font-weight:400;margin-bottom:12px}
.foot-col a{display:block;font-size:11.5px;line-height:21.5px;color:var(--footer-link)}
.social{display:flex!important;align-items:center;gap:9px}
.social span{width:17px;height:17px;border-radius:50%;background:#888}
.social span.sky{background:#5fc8e6}
.copyright{position:absolute;left:146px;top:136px;font-size:10.5px;color:#a9adad}
</style>
</head>
<body>

<header class="site-header">
  <a class="brand brand-header" href="#"><span class="brand-dot"></span>VELTORA</a>
  <a class="login" href="#">Login</a>
  <nav class="main-nav">
    <a class="active" href="#">Features</a>
    <a href="#" style="left:125px">Examples</a>
    <a href="#" style="left:247px">Faq</a>
    <a href="#" style="left:328px">About</a>
  </nav>
</header>

<section class="hero" role="img" aria-label="Misty grey field with two figures walking in the distance">
  <h1 class="hero-title">Smarter Financial Strategies</h1>
  <p class="hero-sub">Values and Cash-flow focused financial software for financial planners.</p>
  <a class="btn btn-gold" href="#">For Planning Practices</a>
  <a class="btn btn-white" href="#">For Dealer Groups</a>
  <div class="video">
    <div class="video-still" role="img" aria-label="Video still of a smiling businessman in a meeting">
      <svg class="video-bar" viewBox="0 0 445 32" preserveAspectRatio="none">
        <rect x="0" y="0" width="53" height="32" rx="2" fill="#2b2f33"/>
        <polygon points="21,8 21,24 35,16" fill="#fff"/>
        <rect x="62" y="6" width="383" height="22" rx="2" fill="#2b2f33"/>
        <rect x="70" y="13" width="308" height="8" fill="#cfd3d6"/>
        <rect x="70" y="13" width="90" height="8" fill="#1e9be0"/>
        <rect x="386" y="12" width="30" height="10" fill="#1e9be0"/>
      </svg>
    </div>
  </div>
</section>

<section class="features">
  <h2 class="intro-title">The standard chunk<br>of Lorem Ipsum</h2>
  <p class="intro-text" style="top:124px">Lorem Ipsum is simply dummy text of the printing and typesetting industry. Lorem Ipsum has been the industry's standard dummy text ever since the 1500s.</p>
  <p class="intro-text" style="top:244px">when an unknown printer took a galley of type and scrambled it to make a type specimen book. It has survived not only five centuries.</p>

  <article class="card" style="left:364px;top:87px">
    <h3>Fact Find</h3>
    <p>Contrary to popular belief, Lorem Ipsum is not text</p>
    <a class="more" href="#">Read more ⟶</a>
    <svg class="icon" viewBox="0 0 48 48"><rect x="6" y="3" width="36" height="42" rx="3" fill="none" stroke="#666" stroke-width="4"/><rect x="13" y="11" width="9" height="8" fill="#666"/><path d="M25 12h10M25 17h10M13 24h22M13 29h22M13 34h22" stroke="#666" stroke-width="3"/></svg>
  </article>
  <article class="card highlight" style="left:582px;top:87px">
    <h3>Online Data</h3>
    <p>Contrary to popular belief, Lorem Ipsum is not text</p>
    <a class="more" href="#">Read more ⟶</a>
    <svg class="icon" viewBox="0 0 48 48"><rect x="2" y="6" width="44" height="30" rx="3" fill="none" stroke="#111" stroke-width="4"/><rect x="14" y="38" width="20" height="4" fill="#111"/></svg>
  </article>
  <article class="card" style="left:800px;top:87px">
    <h3>Custom Branding</h3>
    <p>Contrary to popular belief, Lorem Ipsum is not text</p>
    <a class="more" href="#">Read more ⟶</a>
    <svg class="icon" viewBox="0 0 48 48"><circle cx="24" cy="24" r="19" fill="none" stroke="#666" stroke-width="5"/><circle cx="24" cy="24" r="9" fill="none" stroke="#666" stroke-width="4"/><path d="M11 11l7 7M37 11l-7 7M11 37l7-7M37 37l-7-7" stroke="#666" stroke-width="5"/></svg>
  </article>
  <article class="card" style="left:364px;top:223px">
    <h3>Site Integration</h3>
    <p>Contrary to popular belief, Lorem Ipsum is not text</p>
    <a class="more" href="#">Read more ⟶</a>
    <svg class="icon" viewBox="0 0 48 48"><path d="M12 3h24M12 45h24M14 3c0 14 18 14 18 21s-18 7-18 21M34 3c0 14-18 14-18 21s18 7 18 21" fill="none" stroke="#666" stroke-width="3"/><path d="M17 42c2-6 12-6 14 0z" fill="#666"/></svg>
  </article>
  <article class="card" style="left:582px;top:223px">
    <h3>Upload Files</h3>
    <p>Contrary to popular belief, Lorem Ipsum is not text</p>
    <a class="more" href="#">Read more ⟶</a>
    <svg class="icon" viewBox="0 0 48 48"><path d="M2 30h12v6h20v-6h12v14H2z" fill="#666"/><path d="M24 6l-11 11h7v13h8V17h7z" fill="#666"/></svg>
  </article>
  <article class="card" style="left:800px;top:223px">
    <h3>User Management</h3>
    <p>Contrary to popular belief, Lorem Ipsum is not text</p>
    <a class="more" href="#">Read more ⟶</a>
    <svg class="icon" viewBox="0 0 48 48"><circle cx="16" cy="14" r="8" fill="#666"/><path d="M1 44c0-12 6-18 15-18s15 6 15 18z" fill="#666"/><circle cx="34" cy="18" r="6" fill="#666"/><path d="M33 44c0-8-2-13-5-15 2-2 4-2 6-2 8 0 13 5 13 17z" fill="#666"/></svg>
  </article>

  <div class="divider"></div>
  <p class="cta">Create an account today and begin your 30 day trial!</p>
  <a class="btn-signup" href="#">Sign Up Now !</a>
</section>

<footer class="site-footer">
  <a class="brand brand-footer" href="#"><span class="brand-dot"></span>VELTORA</a>
  <div class="foot-col" style="left:365px">
    <h4>About</h4>
    <a href="#">About Us</a><a href="#">Support</a>
  </div>
  <div class="foot-col" style="left:509px">
    <h4>Getting Started</h4>
    <a href="#">Why Veltora</a><a href="#">Download a Summary</a><a href="#">Veltora Videos</a>
  </div>
  <div class="foot-col" style="left:655px">
    <h4>Legal</h4>
    <a href="#">Terms of Use</a><a href="#">Privacy</a>
  </div>
  <div class="foot-col" style="left:800px">
    <h4>Connect</h4>
    <a class="social" href="#"><span></span>Veltora on Netlink</a>
    <a class="social" href="#"><span class="sky"></span>Veltora on Chirper</a>
  </div>
  <p class="copyright">Copyright © 2014 Veltora Pty Ltd. All rights reserved.</p>
</footer>

</body>
</html>
```